Colin Ashbury Racing

I am a racehorse trainer and wish to produce a business card with my details and logo.
The stable colours are Royal blue and black.
The card would need my name and contact details.
Thanks, Colin.

Target Market(s)

Horse owners

Industry/Entity Type

Business

Font styles to use
Serif

Colors
0555a3

Requirements
Must have
• My name. Colour scheme of blue and black.
Nice to have
• Horse or jockey

```html
<!DOCTYPE html>
<html lang="en">
<head>
<meta charset="utf-8">
<title>Colin Ashbury Racing – Business Card</title>
<link href="https://fonts.googleapis.com/css2?family=Open+Sans:wght@400;700&display=swap" rel="stylesheet">
<style>
  :root {
    --royal-blue: #0555a3;
    --deep-blue: #0a4f9c;
    --stable-black: #111111;
    --paper: #ffffff;
    --backdrop: #e9ebee;
  }
  * { box-sizing: border-box; margin: 0; padding: 0; }
  html, body {
    width: 1200px; height: 900px; overflow: hidden;
    background: var(--backdrop);
    font-family: "Open Sans", Arial, sans-serif;
  }
  .canvas {
    position: relative; width: 1200px; height: 900px;
    display: flex; flex-direction: column; align-items: center;
    justify-content: center; gap: 24px;
  }
  .card {
    position: relative; width: 700px; height: 400px; overflow: hidden;
    box-shadow: 0 6px 18px rgba(0,0,0,0.18);
  }
  /* Back of card */
  .card-back { background: var(--royal-blue); }
  .card-back .back-name {
    position: absolute; right: 48px; bottom: 44px;
    color: var(--paper); font-weight: 700; font-size: 24px;
    letter-spacing: 0.5px; text-transform: uppercase;
  }
  /* Front of card */
  .card-front { background: var(--paper); }
  .card-front .swoosh { position: absolute; inset: 0; }
  .brand-name {
    position: absolute; left: 100px; top: 120px;
    color: var(--royal-blue); font-weight: 700; font-size: 30px;
    text-transform: uppercase; letter-spacing: 0.5px;
  }
  .contact-block {
    position: absolute; right: 36px; top: 222px;
    text-align: right; color: var(--paper);
  }
  .contact-name { font-weight: 700; font-size: 22px; line-height: 1.1; }
  .contact-role { font-size: 20px; line-height: 1.2; margin-bottom: 12px; }
  .contact-line {
    display: flex; align-items: center; justify-content: flex-end;
    gap: 14px; font-size: 18px; height: 33px;
  }
  .contact-icon {
    width: 24px; height: 24px; border-radius: 4px;
    background: var(--paper); display: flex;
    align-items: center; justify-content: center;
  }
  .contact-icon svg { width: 16px; height: 16px; }
</style>
</head>
<body>
<main class="canvas">

  <section class="card card-back" aria-label="Card back">
    <p class="back-name">Colin Ashbury Racing</p>
  </section>

  <section class="card card-front" aria-label="Card front">
    <svg class="swoosh" viewBox="0 0 700 400" width="700" height="400" aria-hidden="true">
      <path d="M0,225 C100,330 260,360 400,270 C490,210 590,150 700,118 L700,400 L0,400 Z" fill="var(--royal-blue)"/>
      <path d="M25,215 C120,318 265,343 398,256 C488,197 590,138 700,106" fill="none" stroke="var(--stable-black)" stroke-width="9"/>
      <path d="M40,285 C150,362 280,376 380,342" fill="none" stroke="var(--paper)" stroke-width="6"/>
      <path d="M70,322 C170,386 290,390 380,366" fill="none" stroke="var(--stable-black)" stroke-width="4"/>
    </svg>

    <p class="brand-name">Colin Ashbury Racing</p>

    <div class="contact-block">
      <p class="contact-name">Colin</p>
      <p class="contact-role">Race Management</p>
      <p class="contact-line">555 014 2386
        <span class="contact-icon"><svg viewBox="0 0 16 16"><path d="M4 1.5 L6.5 4 L5 5.8 C6 8 8 10 10.2 11 L12 9.5 L14.5 12 L12.5 14.5 C7 14 2 9 1.5 3.5 Z" fill="var(--deep-blue)"/></svg></span>
      </p>
      <p class="contact-line">www.colinashburyr.com
        <span class="contact-icon"><svg viewBox="0 0 16 16"><circle cx="8" cy="8" r="6" fill="none" stroke="var(--deep-blue)" stroke-width="1.5"/><ellipse cx="8" cy="8" rx="2.6" ry="6" fill="none" stroke="var(--deep-blue)" stroke-width="1.2"/><line x1="2" y1="8" x2="14" y2="8" stroke="var(--deep-blue)" stroke-width="1.2"/></svg></span>
      </p>
      <p class="contact-line">info@colinashburyr.com
        <span class="contact-icon"><svg viewBox="0 0 16 16"><text x="8" y="12.5" text-anchor="middle" font-family="Open Sans, Arial, sans-serif" font-weight="700" font-size="13" fill="var(--deep-blue)">@</text></svg></span>
      </p>
    </div>
  </section>

</main>
</body>
</html>
```